Surface Protection company needs cards

We are a New Zealand company that will apply nanotechnology coatings on surfaces to prevent growth and spread of bacteria, viruses, mold etc with a sprayer. We deal with large corporates, airlines, hospitals and schools so we are after a new modern, simple and clean look that will have great visual impact.
We a company that is focused on prevention and protection.

Company name, Vela Shield

Subtext, Antimicrobial Surface Protection

Logo, VS

Target Market(s)

Hospitals, Transport agencies, Airlines, Corporate entities

Contact Information for Business Card

Company name, VelaShield
Logo, VS

Garth Ormsby
velashieldnz@postkite.example
+64219302648
www.velashield.example.nz

Requirements
Must have
• Simple clean look.
Nice to have
• We apply nano coatings so try and incorporate this into a theme somehow

```html
<!DOCTYPE html>
<html lang="en">
<head>
<meta charset="utf-8">
<title>VelaShield Business Cards</title>
<link rel="stylesheet" href="https://fonts.googleapis.com/css2?family=Michroma&family=Montserrat:wght@300;400&family=Oswald:wght@500&family=Open+Sans:wght@400&display=swap">
<style>
  :root {
    --backdrop: #1d1d20;
    --card: #ffffff;
    --ink: #3a3a3d;
    --ink-dark: #1f1f22;
    --ink-soft: #55555a;
    --rule: #8a8a8f;
  }
  * { box-sizing: border-box; margin: 0; padding: 0; }
  html, body {
    width: 1200px;
    height: 799px;
    overflow: hidden;
    background: var(--backdrop);
  }
  .stage {
    position: relative;
    width: 1200px;
    height: 799px;
  }
  .card {
    position: absolute;
    top: 251px;
    width: 520px;
    height: 297px;
    background: var(--card);
  }
  .card--front { left: 55px; }
  .card--back { left: 625px; }

  /* Front */
  .brand {
    position: absolute;
    inset: 0;
    display: flex;
    flex-direction: column;
    align-items: center;
    justify-content: center;
  }
  .brand__name {
    font-family: "Michroma", sans-serif;
    font-size: 36px;
    color: var(--ink);
    letter-spacing: 0.02em;
    line-height: 1;
  }
  .brand__tagline {
    margin-top: 14px;
    font-family: "Montserrat", sans-serif;
    font-weight: 300;
    font-size: 11.5px;
    letter-spacing: 0.3em;
    color: var(--ink-soft);
    text-transform: uppercase;
  }

  /* Back */
  .person {
    position: absolute;
    right: 292px;
    top: 112px;
    text-align: right;
  }
  .person__name {
    font-family: "Oswald", sans-serif;
    font-weight: 500;
    font-size: 25px;
    color: var(--ink-dark);
    text-transform: uppercase;
    line-height: 1.05;
    letter-spacing: 0.01em;
  }
  .person__role {
    font-family: "Open Sans", sans-serif;
    font-size: 12px;
    color: var(--ink-soft);
    margin-top: 2px;
  }
  .divider {
    position: absolute;
    left: 244px;
    top: 92px;
    width: 1px;
    height: 86px;
    background: var(--rule);
  }
  .contacts {
    position: absolute;
    left: 262px;
    top: 98px;
    list-style: none;
  }
  .contacts li,
  .address {
    display: flex;
    align-items: center;
    gap: 8px;
    font-family: "Open Sans", sans-serif;
    font-size: 12px;
    color: var(--ink-dark);
    height: 24px;
  }
  .icon {
    width: 11px;
    height: 11px;
    flex: none;
    fill: var(--ink-dark);
  }
  .address {
    position: absolute;
    left: 190px;
    bottom: 34px;
  }
</style>
</head>
<body>
<main class="stage">
  <section class="card card--front" aria-label="Business card front">
    <div class="brand">
      <div class="brand__name">VELASHIELD</div>
      <div class="brand__tagline">Antimicrobial Surface Protection</div>
    </div>
  </section>

  <section class="card card--back" aria-label="Business card back">
    <div class="person">
      <div class="person__name">Garth Ormsby</div>
      <div class="person__role">Director</div>
    </div>
    <div class="divider"></div>
    <ul class="contacts">
      <li>
        <svg class="icon" viewBox="0 0 24 24" aria-hidden="true"><path d="M6.6 10.8a15.1 15.1 0 0 0 6.6 6.6l2.2-2.2a1 1 0 0 1 1-.25 11.4 11.4 0 0 0 3.6.57 1 1 0 0 1 1 1V20a1 1 0 0 1-1 1A17 17 0 0 1 3 4a1 1 0 0 1 1-1h3.5a1 1 0 0 1 1 1c0 1.25.2 2.45.57 3.57a1 1 0 0 1-.25 1z"/></svg>
        +64219302648
      </li>
      <li>
        <svg class="icon" viewBox="0 0 24 24" aria-hidden="true"><path d="M2 5h20v14H2z M3.5 6.5 12 13l8.5-6.5" fill="none" stroke="#1f1f22" stroke-width="0"/><path d="M2 5h20v2.2l-10 6.6L2 7.2z"/><path d="M2 9.4l10 6.6 10-6.6V19H2z"/></svg>
        velashieldnz@postkite.example
      </li>
      <li>
        <svg class="icon" viewBox="0 0 24 24" aria-hidden="true"><path d="M12 2a10 10 0 1 0 0 20 10 10 0 0 0 0-20zm6.9 6h-2.8a15 15 0 0 0-1.3-3.6A8 8 0 0 1 18.9 8zM12 4c.8 1.1 1.5 2.5 1.9 4h-3.8c.4-1.5 1.1-2.9 1.9-4zM4.3 14a8 8 0 0 1 0-4h3.2a16 16 0 0 0 0 4zm.8 2h2.8c.3 1.3.8 2.5 1.3 3.6A8 8 0 0 1 5.1 16zm2.8-8H5.1a8 8 0 0 1 4.1-3.6C8.7 5.5 8.2 6.7 7.9 8zM12 20c-.8-1.1-1.5-2.5-1.9-4h3.8c-.4 1.5-1.1 2.9-1.9 4zm2.3-6H9.7a14 14 0 0 1 0-4h4.6a14 14 0 0 1 0 4zm.5 5.6c.5-1.1 1-2.3 1.3-3.6h2.8a8 8 0 0 1-4.1 3.6zm1.7-5.6a16 16 0 0 0 0-4h3.2a8 8 0 0 1 0 4z"/></svg>
        www.velashield.example.nz
      </li>
    </ul>
    <div class="address">
      <svg class="icon" viewBox="0 0 24 24" aria-hidden="true"><path d="M12 2a7 7 0 0 0-7 7c0 5.2 7 13 7 13s7-7.8 7-13a7 7 0 0 0-7-7zm0 9.5a2.5 2.5 0 1 1 0-5 2.5 2.5 0 0 1 0 5z"/></svg>
      421, Address line here Country Name, 45452
    </div>
  </section>
</main>
</body>
</html>
```